Hip, Modern Home Page for Successful SEO Expert

Marcus Delwyn is an SEO expert, author and professional speaker. His site is
www.marcusdelwyn.net. We need a re-design of the website so that it does not look outdated or like an off-the-shelf Wordpress template (like it currently does). The new design must convey to the visitor a compelling call-to-action. Specially, this home page will act as a “squeeze page” and thus, the primary marketing goal will be to get the user to opt in to our list. The new design will provide elements of “social proof” such as written testimonials, a portfolio of case studies, client logos, “as appeared on” logos, client testimonial video, etc.
Updates

Please incorporate the recently uploaded headshots into your design 

Target Market(s)

People looking for help in internet marketing for their websites, entrepreneurs, start-ups, bloggers, companies looking to build an online presence, conferences looking to book Marcus for speaking. Small business people and SEO newbies interested in buying Marcus’s video-based training (RankCraftLab.net).

Industry/Entity Type

Marketing

Font styles to use
Sans Serif

Colors
f68d4d
3276b5
8769ae
acd036

Requirements
Must have
• strong call to action
Should not have
• should not look like a template. should not use old style fonts. should not have more than one page scroll

```html
<!DOCTYPE html>
<html lang="en">
<head>
<meta charset="utf-8">
<title>Marcus Delwyn website – homepage idea two</title>
<link rel="stylesheet" href="https://fonts.googleapis.com/css2?family=Josefin+Sans:wght@400&family=Lato:ital,wght@0,300;0,400;0,700;1,400;1,700&display=swap">
<style>
  :root{
    --ink:#1d1d1d;
    --grey:#6d6d6d;
    --rule:#9a9a9a;
    --blue:#3f66b5;
    --link:#2f5aa8;
    --nav-line:#7f96d0;
    --orange:#f68d4d;
    --panel:#1f1f1f;
    --paper:#ffffff;
  }
  *{box-sizing:border-box;margin:0;padding:0}
  html,body{width:1200px;height:927px;overflow:hidden;background:var(--paper)}
  body{font-family:"Lato",sans-serif;color:var(--ink)}
  .board{position:absolute;left:0;top:0;width:1100px;height:850px;transform:scale(1.090909);transform-origin:0 0}
  .board-label{position:absolute;left:28px;top:24px;font-family:"Josefin Sans",sans-serif;font-size:22px}
  .board-title{position:absolute;left:0;width:1100px;top:72px;text-align:center;font-family:"Josefin Sans",sans-serif;font-size:23px;letter-spacing:.3px}
  .page{position:absolute;left:342px;top:118px;width:416px;height:677px;border:1.5px solid var(--ink)}
  .page > *{position:absolute}

  .brand-dot{left:17px;top:24px;width:14px;height:14px;border-radius:50%;background:var(--blue)}
  .brand{left:37px;top:22px;font-size:14px;font-weight:400;line-height:18px;color:var(--blue);white-space:nowrap}
  .roles{left:37px;top:44px;font-size:8.5px;line-height:10.5px;color:var(--grey);letter-spacing:.6px}
  .vrule{width:1px;background:var(--rule)}
  .pull{left:186px;top:19px;width:96px;text-align:right;color:var(--blue)}
  .pull q{display:block;font-style:italic;font-size:11.5px;line-height:11px;quotes:"\201C" "\201D"}
  .pull cite{display:block;font-style:normal;font-weight:700;font-size:5.5px;line-height:7px;margin-top:2px}
  .more{color:var(--orange);font-weight:700;font-size:6.5px;letter-spacing:.3px}
  .pull .more{display:block;margin-top:7px}
  .search{left:296px;top:21px;width:90px;height:12px;border:1px solid var(--grey);font-size:6px;color:var(--grey);padding:2px 3px}
  .search-icon{left:390px;top:20px}
  .social{display:flex;gap:13px}
  .social span{width:14px;height:14px;background:var(--ink)}
  .band{left:17px;width:382px;height:14px;background:var(--ink)}

  .nav{left:17px;top:98px;width:70px;list-style:none}
  .nav li{height:17.3px;border:1px solid var(--nav-line);border-top:none;font-size:7px;letter-spacing:.5px;color:#555;padding:4px 3px}
  .nav li:first-child{border-top:1px solid var(--nav-line)}
  .optin{left:17px;top:244px;width:70px;height:42px;border:1px solid var(--rule);font-size:6.5px;line-height:8.5px;color:#8a8a8a;padding:3px 3px;letter-spacing:.3px}
  .subscribe{left:17px;top:288px;width:70px;height:34px;background:var(--orange);border:1px solid #b06034;font-size:6.5px;line-height:8.5px;color:#6b2f10;padding:8px 3px;letter-spacing:.3px}
  .invite{left:17px;top:329px;width:70px;height:34px;background:var(--panel);color:#fff;font-size:6.5px;line-height:8px;padding:4px 3px;letter-spacing:.3px}
  .invite svg{position:absolute;right:4px;top:8px}

  .press{left:17px;top:377px;width:70px}
  .press article{border-top:1px solid var(--rule);padding:9px 0 0;height:69px}
  .press article:last-child{border-bottom:1px solid var(--rule);height:60px}
  .outlet{display:flex;align-items:center;gap:3px;font-size:8px;font-weight:700;color:var(--blue);height:18px}
  .outlet i{display:inline-block;width:10px;height:10px;background:var(--blue)}
  .press h4{font-size:6px;line-height:7.5px;font-style:italic;font-weight:700;margin-top:3px}
  .press .more{display:block;font-size:6px;font-weight:400}

  .hero{left:96px;top:98px;width:303px;height:121px;background:linear-gradient(90deg,#7b6a5a 0%,#a49a8e 30%,#d6d4ce 55%,#cfcdc7 100%)}
  .hero-quote{left:220px;top:122px;width:160px;text-align:center;font-style:italic;font-size:7.3px;line-height:10px;letter-spacing:.4px;color:#222}
  .hero-quote cite{display:block;font-style:normal;font-size:5px;line-height:6px;margin-top:2px;letter-spacing:.3px}
  .dots{left:260px;top:200px;display:flex;gap:3px}
  .dots span{width:10px;height:10px;border-radius:50%;background:#e8e8e8;border:1px solid #bbb}
  .dots span:first-child{background:#2a2a2a;border:2px solid #8fa83a}

  .intro{left:97px;top:225px;width:199px;height:138px;background:var(--blue);color:#fff;font-size:11px;line-height:16px;font-weight:300;padding:6px 4px}
  .events{left:97px;top:377px;width:199px;border-top:1px solid var(--rule);padding-top:10px}
  .events h2{font-size:11.5px;font-weight:400;letter-spacing:1.2px;line-height:16px}
  .events dl{margin-top:16px}
  .events dt{font-size:8.3px;color:var(--grey);line-height:11px}
  .events dd{font-size:8.3px;line-height:11px;color:var(--grey);margin-bottom:14px}
  .events dd b{color:var(--link);font-weight:700}
  .events .more{font-size:8px}

  .book{left:302px;width:97px;background:var(--panel);color:#fff;padding:6px 5px}
  .cover{width:86px;height:117px}
  .book h3{font-size:6.5px;font-style:italic;font-weight:700;margin-top:10px}
  .book p{font-size:6.3px;line-height:8px;margin-top:1px}
  .book .more{display:block;margin-top:2px}

  .copyright{left:26px;top:662px;font-size:6.5px;color:var(--grey);letter-spacing:.6px}
</style>
</head>
<body>
<div class="board">
  <div class="board-label">Marcus Delwyn webiste</div>
  <div class="board-title">HOMEPAGE - IDEA TWO - NAME OPTION 1</div>

  <main class="page">
    <div class="brand-dot"></div>
    <div class="brand">Marcus Delwyn</div>
    <div class="roles">SEO Expert<br>Author<br>Professional Speaker</div>
    <div class="vrule" style="left:182px;top:14px;height:60px"></div>
    <div class="pull">
      <q>MARCUS IS THE SEO MASTER</q>
      <cite>JORDAN VALE, SUPER BLOGGER,<br>JORDANVALE.COM</cite>
      <span class="more">READ MORE &gt;&gt;</span>
    </div>
    <div class="vrule" style="left:286px;top:14px;height:60px"></div>
    <div class="search">Search</div>
    <svg class="search-icon" width="14" height="14" viewBox="0 0 14 14" aria-hidden="true"><circle cx="5.5" cy="5.5" r="4" fill="none" stroke="#1d1d1d" stroke-width="1.4"/><line x1="8.5" y1="8.5" x2="13" y2="13" stroke="#1d1d1d" stroke-width="1.8"/></svg>
    <div class="social" style="left:296px;top:63px" aria-label="Social links"><span></span><span></span><span></span><span></span></div>

    <div class="band" style="top:84px"></div>

    <ul class="nav">
      <li>BIOGRAPHY</li><li>BOOKS</li><li>ARTICLES</li><li>SPEAKING</li>
      <li>INTERVIEWS</li><li>TESTIMONIALS</li><li>IN THE NEWS</li><li>BLOG</li>
    </ul>
    <div class="optin">ENTER YOUR EMAIL HERE TO SUBSCRIBE TO OUR E-NEWS</div>
    <div class="subscribe">SUBSCRIBE TO OUR E-NEWS</div>
    <div class="invite">INVITE<br>MARCUS<br>TO SPEAK
      <svg width="26" height="20" viewBox="0 0 26 20" aria-hidden="true"><path d="M0 0 L26 10 L0 20 L8 10 Z" fill="#3f66b5"/></svg>
    </div>

    <div class="press">
      <article>
        <div class="outlet"><i></i>blog.retailhub</div>
        <h4>Seven Tips to Get a Grip on ClipTube SEO</h4>
        <span class="more">READ MORE...</span>
      </article>
      <article>
        <div class="outlet"><i></i>Promo Harbor</div>
        <h4>Leveregine Memes for your Own Viral Marketing</h4>
        <span class="more">READ MORE...</span>
      </article>
      <article>
        <div class="outlet"><i></i>Query Field</div>
        <h4>The Secret Life of the Black Hat SEO</h4>
        <span class="more">READ MORE...</span>
      </article>
    </div>

    <div class="hero" role="img" aria-label="Headshot of Marcus Delwyn smiling, in a blue shirt and dark vest, on a soft grey background"></div>
    <blockquote class="hero-quote">“MARCUS HAS A REAL ENTHUSIASM FOR THE POWER OF THE INTERNET TO CHANGE BUSINESSES AND HIS PASSION RUBS OFF ON YOU.”
      <cite>DALE HARTWICK<br>MANAGING DIRECTOR, BRIGHTPATH</cite>
    </blockquote>
    <div class="dots"><span></span><span></span><span></span><span></span><span></span><span></span></div>

    <p class="intro">Marcus Delwyn has over 15 years experience in SEO and internet success. He invented FlowRank, an automated pay-for-performance SEO technology. He is an SEO Expert, Author of two successful books and several articles on the subject, and an International Professional Speaker.</p>

    <section class="events">
      <h2>MARCUS’S UPCOMING APPEARANCES:</h2>
      <dl>
        <dt>September 26 - 27, 2013</dt><dd><b>MAA : SEO in 2013</b> Chicago, Illinois</dd>
        <dt>September 30 - October 2, 2013</dt><dd><b>RetailHub Annual Summit</b> Chicago, Illinios</dd>
        <dt>October 9 -11, 2103</dt><dd><b>ReachPros B2B Marketing Forum</b><br>Boston, MA</dd>
        <dt>October 21-24, 2013</dt><dd><b>NetCon</b> Las Vegas, NV</dd>
      </dl>
      <span class="more">READ MORE »</span>
    </section>

    <article class="book" style="top:225px;height:197px">
      <div class="cover" role="img" aria-label="Book cover of The Craft of Search with a hummingbird on a green background" style="background:linear-gradient(160deg,#3d7a2e,#7fb13c 45%,#b33a7a)"></div>
      <h3>The Craft of Search</h3>
      <p>To be successful in a virtual economy, it’s vital to optimize your site for search engine visibility.</p>
      <span class="more">READ MORE...</span>
    </article>
    <article class="book" style="top:427px;height:197px">
      <div class="cover" role="img" aria-label="Book cover of Deep Query Search with an engraved bird above a teal title band" style="background:linear-gradient(180deg,#f2f2f2 0%,#cfcfcf 62%,#26b0b3 63%,#26b0b3 82%,#f2f2f2 83%)"></div>
      <h3>Deep Query Search</h3>
      <p>Behind Querynet’s deceptively simple interface is immense power for both market and competitive research - if you know how to use it well.</p>
      <span class="more">READ MORE...</span>
    </article>

    <div class="band" style="top:631px"></div>
    <p class="copyright">© 2014 Marcus Delwyn. All Rights Reserved.</p>
    <div class="social" style="left:306px;top:655px;gap:6px" aria-label="Social links"><span></span><span></span><span></span><span></span></div>
  </main>
</div>
</body>
</html>
```